Boutique custom software development company needs new business card

Our nearly 20 year old custom software development company would like to better include the fact that we are now providing Bitcoin services. These new services are B2B include education (how to acquire and securely hold Bitcoin) and integrating Bitcoin payments into existing ecommerce sites or other existing systems. Please keep the card clean and simple. Attached is our current design and some other files. vexalon.example

Target Market(s)

businesses owners interested in long term relationship

Industry/Entity Type

Custom software development and Bitcoin

Contact Information for Business Card

Marcus Ellwood, marcus@vexalon.example, vexalon.example, (888) 555-VEXAL

Font styles to use
Other font styles liked:
• monospace

Requirements
Must have
• double-sided
Nice to have
• clean and simple
Should not have
• physical address

```html
<!DOCTYPE html>
<html lang="en">
<head>
<meta charset="utf-8">
<title>Vexalon business card</title>
<link rel="stylesheet" href="https://fonts.googleapis.com/css2?family=Courier+Prime:wght@400;700&display=swap">
<style>
  :root {
    --page: #e9eaec;
    --card-light: #eef0f3;
    --card-white: #f7f8fa;
    --brand-blue: #1b52b5;
    --brand-orange: #ea640c;
    --ink-white: #ffffff;
    --rule: rgba(255, 255, 255, 0.45);
  }
  * { margin: 0; padding: 0; box-sizing: border-box; }
  html, body {
    width: 1200px;
    height: 740px;
    overflow: hidden;
    background: var(--page);
  }
  .stage {
    position: relative;
    width: 1200px;
    height: 740px;
  }
  .card {
    position: absolute;
    top: 220px;
    width: 525px;
    height: 300px;
    border-radius: 22px;
    overflow: hidden;
    box-shadow: 0 10px 26px rgba(0, 0, 0, 0.16);
  }
  .card--front { left: 50px; }
  .card--back {
    left: 625px;
    background: var(--brand-blue);
    display: flex;
    flex-direction: column;
    align-items: center;
    justify-content: center;
    gap: 10px;
  }
  .card svg { display: block; }
  .card-text {
    font-family: "Courier Prime", "Courier New", monospace;
    font-weight: 700;
  }
  .back-name {
    font-family: "Courier Prime", "Courier New", monospace;
    font-weight: 700;
    font-size: 46px;
    line-height: 1;
    color: var(--ink-white);
    letter-spacing: 2px;
  }
  .back-tagline {
    font-family: "Courier Prime", "Courier New", monospace;
    font-weight: 400;
    font-size: 18px;
    line-height: 1.2;
    color: var(--ink-white);
  }
</style>
</head>
<body>
<main class="stage">

  <section class="card card--front" aria-label="Front of card">
    <svg width="525" height="300" viewBox="0 0 525 300">
      <rect class="front-base" width="525" height="300" fill="var(--card-light)"/>
      <path class="front-sheen" d="M0 0 H300 L180 300 H0 Z" fill="var(--card-white)"/>

      <path class="web-band" d="M0 212 H215 Q232 212 238 228 L260 300 H0 Z" fill="var(--brand-orange)"/>

      <circle class="contact-arc" cx="560" cy="210" r="299" fill="none" stroke="var(--brand-orange)" stroke-width="5"/>
      <circle class="contact-panel" cx="560" cy="210" r="290" fill="var(--brand-blue)"/>

      <rect class="brand-square" x="44" y="62" width="26" height="26" fill="var(--brand-blue)"/>
      <text class="card-text brand-name" x="80" y="84" font-size="30" fill="var(--brand-blue)">Vexalon</text>

      <text class="card-text web-address" x="22" y="262" font-size="19" fill="var(--ink-white)">vexalon.example</text>

      <g class="contact-rules" stroke="var(--rule)" stroke-width="1">
        <line x1="340" y1="72" x2="505" y2="72"/>
        <line x1="318" y1="117" x2="505" y2="117"/>
        <line x1="302" y1="162" x2="505" y2="162"/>
        <line x1="290" y1="246" x2="505" y2="246"/>
        <line x1="290" y1="280" x2="505" y2="280"/>
      </g>

      <g class="icon icon-person">
        <circle cx="318" cy="50" r="14" fill="var(--ink-white)" stroke="var(--brand-blue)" stroke-width="2"/>
        <circle cx="318" cy="46" r="4" fill="var(--brand-blue)"/>
        <path d="M311 57 Q318 48 325 57 Z" fill="var(--brand-blue)"/>
      </g>
      <g class="icon icon-mail">
        <circle cx="294" cy="95" r="14" fill="var(--ink-white)" stroke="var(--brand-blue)" stroke-width="2"/>
        <rect x="286" y="89" width="16" height="11" fill="var(--brand-blue)"/>
        <path d="M286 89 L294 95 L302 89" fill="none" stroke="var(--ink-white)" stroke-width="1.2"/>
      </g>
      <g class="icon icon-phone">
        <circle cx="279" cy="140" r="14" fill="var(--ink-white)" stroke="var(--brand-blue)" stroke-width="2"/>
        <path d="M274 133 Q272 136 275 142 Q279 148 284 147 L286 145 L282 141 L280 143 Q277 140 277 137 L279 135 L276 132 Z" fill="var(--brand-blue)"/>
      </g>

      <g class="card-text contact-details" fill="var(--ink-white)">
        <text class="contact-name" x="340" y="59" font-size="20">Marcus Ellwood</text>
        <text class="contact-email" x="316" y="102" font-size="14">marcus@vexalon.example</text>
        <text class="contact-phone" x="300" y="147" font-size="15">(888) 555-VEXAL</text>
      </g>
    </svg>
  </section>

  <section class="card card--back" aria-label="Back of card">
    <span class="back-name">Vexalon</span>
    <span class="back-tagline">Custom Software &amp; Bitcoin Services</span>
  </section>

</main>
</body>
</html>
```